Kestrel Plumbing business card full re design & logo design

Kestrel Plumbing is a Sydney based mechanical plumbing contractor company.
We would like a full redesign with new logo etc which we can take to a future website, uniforms, vehicle sign writing etc.
Blue is my preferred choice of colour but i would be open to see a couple of alternatives thrown in the mix to see how they compare. I am open to see on white cards, black cards etc. Open to many new ideas.
Please see attached original business cards which have been used for the last 5 years.

Target Market(s)

Mechanical services industry.

Industry/Entity Type

Plumbing

Contact Information for Business Card

Dale Fenmore
Director

Mob: 0427 596 418
Email: dale@kestrelplumbing-demo.net.au
PO BOX 782
Harwood Vale NSW 2199
Lic: 518604k

Logo Text

Kestrel Plumbing

Font styles to use
Sans Serif

Colors
0655a3
3276b5
0792cd
33a6d7
85cae6
000000
333333
474747

Requirements
Must have
• Things that make it very professional and very well presented.
Nice to have
• Same description or very similar to attached uploaded file
Should not have
• Anything that makes it look unprofessional or cartoony.

```html
<!DOCTYPE html>
<html lang="en">
<head>
<meta charset="utf-8">
<title>Kestrel Plumbing – Business Card</title>
<link rel="stylesheet" href="https://fonts.googleapis.com/css2?family=Arimo:wght@400;700&family=Source+Sans+3:wght@400;600&display=swap">
<style>
  :root {
    --navy: #1e3f96;
    --blue-deep: #0655a3;
    --blue-mid: #0792cd;
    --cyan: #00aeef;
    --sky: #33a6d7;
    --ink-grey: #58595b;
    --band-grey: #6d6e71;
    --white: #ffffff;
    --stage: #151515;
  }
  * { margin: 0; padding: 0; box-sizing: border-box; }
  html, body { width: 999px; height: 1200px; overflow: hidden; }
  body {
    position: relative;
    background: radial-gradient(ellipse at 50% 50%, #5a5a5a 0%, #2a2a2a 55%, var(--stage) 100%);
    font-family: "Arimo", Arial, sans-serif;
  }
  .card {
    position: absolute;
    left: 64px;
    width: 870px;
    height: 498px;
    overflow: hidden;
  }
  .card--front { top: 74px; background: var(--white); }
  .card--back {
    top: 637px;
    background: linear-gradient(180deg, var(--cyan) 0%, var(--blue-deep) 70%, var(--navy) 100%);
    color: var(--white);
  }

  /* Front */
  .brand-name {
    position: absolute;
    left: 0; top: 228px;
    width: 416px;
    text-align: center;
    font-family: "Arimo", Arial, sans-serif;
    font-weight: 700;
    font-size: 40px;
    line-height: 46px;
    color: var(--blue-deep);
    letter-spacing: 1px;
  }
  .person { position: absolute; left: 461px; top: 56px; }
  .person__name {
    font-family: "Source Sans 3", "Myriad Pro", sans-serif;
    font-weight: 600; font-size: 39px; line-height: 44px;
    color: var(--sky);
  }
  .person__role {
    font-family: "Source Sans 3", "Myriad Pro", sans-serif;
    font-size: 23px; line-height: 30px; color: var(--sky);
  }
  .contact { position: absolute; left: 461px; list-style: none; }
  .contact__row {
    position: absolute; left: 0; white-space: nowrap;
    font-size: 22px; line-height: 30px; color: var(--ink-grey);
  }
  .contact__row svg { position: absolute; left: 0; top: 4px; width: 24px; height: 24px; }
  .contact__row span { position: absolute; left: 42px; top: 0; }
  .footer-band { position: absolute; left: 0; top: 0; }
  .licence {
    position: absolute; right: 40px; top: 435px;
    font-size: 21px; color: var(--white);
  }

  /* Back */
  .services-title {
    position: absolute; left: 0; right: 0; top: 40px;
    text-align: center; font-weight: 700; font-size: 31px;
  }
  .brand-watermark {
    position: absolute; left: 48px; top: 166px;
    width: 500px;
    font-weight: 700; font-size: 80px; line-height: 94px;
    color: rgba(255,255,255,0.55);
    letter-spacing: 1px;
  }
  .specialties { position: absolute; left: 586px; top: 122px; }
  .specialties__title { font-weight: 700; font-size: 30px; line-height: 36px; }
  .specialties__list { list-style: none; margin-top: 2px; }
  .specialties__item {
    position: relative; padding-left: 48px;
    font-size: 23px; line-height: 36px;
  }
  .specialties__item svg { position: absolute; left: 4px; top: 12px; width: 14px; height: 12px; }
  .tagline {
    position: absolute; left: 0; right: 0; top: 408px;
    text-align: center; font-weight: 700; font-size: 31px;
  }
</style>
</head>
<body>

<section class="card card--front" aria-label="Business card front">
  <div class="brand-name">KESTREL<br>PLUMBING</div>

  <div class="person">
    <div class="person__name">Dale Fenmore</div>
    <div class="person__role">Director</div>
  </div>

  <ul class="contact">
    <li class="contact__row" style="top:178px">
      <svg viewBox="0 0 24 24"><path d="M12 1a8 8 0 0 0-8 8c0 6 8 14 8 14s8-8 8-14a8 8 0 0 0-8-8zm0 11a3 3 0 1 1 0-6 3 3 0 0 1 0 6z" fill="var(--blue-mid)"/></svg>
      <span>PO BOX 782<br>Harwood Vale NSW 2199</span>
    </li>
    <li class="contact__row" style="top:267px">
      <svg viewBox="0 0 24 24"><path d="M6 3l3 0 2 5-2 2c1 2 3 4 5 5l2-2 5 2v3c0 1-1 2-2 2C10 20 4 14 4 5c0-1 1-2 2-2z" fill="none" stroke="var(--blue-mid)" stroke-width="2"/><path d="M14 4a6 6 0 0 1 6 6M14 8a2 2 0 0 1 2 2" fill="none" stroke="var(--blue-mid)" stroke-width="2"/></svg>
    </li>
    <li class="contact__row" style="top:305px">
      <svg viewBox="0 0 24 24"><rect x="5" y="2" width="14" height="20" rx="2" fill="none" stroke="var(--blue-mid)" stroke-width="2.4"/><path d="M10 8l4-2M10 13l4-2" stroke="var(--blue-mid)" stroke-width="1.6"/></svg>
      <span>0427 596 418</span>
    </li>
    <li class="contact__row" style="top:341px">
      <svg viewBox="0 0 24 24"><path d="M2 10l10-7 10 7v11H2z" fill="var(--blue-mid)"/><path d="M2 10l10 6 10-6" fill="none" stroke="var(--white)" stroke-width="1.6"/></svg>
      <span>dale@kestrelplumbing-demo.net.au</span>
    </li>
    <li class="contact__row" style="top:377px">
      <svg viewBox="0 0 24 24"><g fill="none" stroke="var(--blue-mid)" stroke-width="1.5"><circle cx="12" cy="12" r="9"/><ellipse cx="12" cy="12" rx="4" ry="9"/><path d="M3 12h18M5 7h14M5 17h14"/></g></svg>
      <span>www.kestrelplumbing-demo.net.au</span>
    </li>
  </ul>

  <svg class="footer-band" width="870" height="498" viewBox="0 0 870 498" aria-hidden="true">
    <defs>
      <linearGradient id="bandBlue" x1="0" y1="0" x2="1" y2="0">
        <stop offset="0" stop-color="#00aeef"/>
        <stop offset="0.6" stop-color="#0071bc"/>
        <stop offset="1" stop-color="#1e3f96"/>
      </linearGradient>
    </defs>
    <rect x="0" y="426" width="870" height="40" fill="var(--band-grey)"/>
    <path d="M0 463 H440 C480 463 490 418 540 418 H870 V498 H0 Z" fill="url(#bandBlue)"/>
  </svg>
  <div class="licence">Lic: 518604k</div>
</section>

<section class="card card--back" aria-label="Business card back">
  <h2 class="services-title">Mechanical Plumbing Services</h2>

  <div class="brand-watermark">KESTREL<br>PLUMBING</div>

  <div class="specialties">
    <h3 class="specialties__title">Specialising in:</h3>
    <ul class="specialties__list">
      <li class="specialties__item"><svg viewBox="0 0 14 12"><path d="M0 0l6 6-6 6zM7 0l6 6-6 6z" fill="var(--white)"/></svg>Make Good</li>
      <li class="specialties__item"><svg viewBox="0 0 14 12"><path d="M0 0l6 6-6 6zM7 0l6 6-6 6z" fill="var(--white)"/></svg>Refurbishment</li>
      <li class="specialties__item"><svg viewBox="0 0 14 12"><path d="M0 0l6 6-6 6zM7 0l6 6-6 6z" fill="var(--white)"/></svg>Tenancy Fit Out</li>
      <li class="specialties__item"><svg viewBox="0 0 14 12"><path d="M0 0l6 6-6 6zM7 0l6 6-6 6z" fill="var(--white)"/></svg>Plant Room Works</li>
      <li class="specialties__item"><svg viewBox="0 0 14 12"><path d="M0 0l6 6-6 6zM7 0l6 6-6 6z" fill="var(--white)"/></svg>Shut Downs</li>
      <li class="specialties__item"><svg viewBox="0 0 14 12"><path d="M0 0l6 6-6 6zM7 0l6 6-6 6z" fill="var(--white)"/></svg>Change Overs</li>
    </ul>
  </div>

  <p class="tagline">Kestrel have the Solution</p>
</section>

</body>
</html>
```